Request for Business Card Design

Hi. My name is Marlena, I am looking for a new business card design for my company, Quorvane Sensing Systems, LLC. I really like the design you did for Tessaly Harvest and was hoping you could do something similar using our full logo and our mark. I am also open to any raised texture design using our mark. I have attached our full logo, which would need to be somewhere on the card, as well as the mark in both outline and full form, as well as our brand colors / guide. The card does not have to be white, as long as our logo and mark appear. I actually like darker colored business cards more, but am open to all options. If you are interested in working with me, please let me know. We would also take the business card design into letterhead design if you can do that.

```html
<!DOCTYPE html>
<html lang="en">
<head>
<meta charset="utf-8">
<title>Quorvane Sensing Systems — Business Card</title>
<link rel="stylesheet" href="https://fonts.googleapis.com/css2?family=Montserrat:wght@400;500;700;800&display=swap">
<style>
  :root {
    --brand-blue: #0e9abf;
    --ink: #3b3b3d;
    --paper: #ffffff;
    --stage: #e9ebee;
    --card-w: 620px;
    --card-h: 354px;
  }
  * { box-sizing: border-box; margin: 0; padding: 0; }
  html, body {
    width: 1200px; height: 927px; overflow: hidden;
    background: var(--stage);
    font-family: "Montserrat", Arial, sans-serif;
  }
  .sheet {
    width: 1200px; height: 927px;
    display: flex; flex-direction: column; align-items: center; justify-content: center;
    gap: 72px;
  }
  .card {
    position: relative;
    width: var(--card-w); height: var(--card-h);
    border-radius: 22px;
    overflow: hidden;
    box-shadow: 0 6px 20px rgba(0,0,0,0.12);
  }

  /* Front side */
  .card--front {
    background: var(--brand-blue);
    display: flex; align-items: center; justify-content: center;
  }
  .wordmark {
    display: flex; align-items: center; gap: 18px;
    font-weight: 700;
  }
  .wordmark__dot {
    width: 46px; height: 46px; border-radius: 50%;
    background: currentColor; flex: none;
  }
  .wordmark__text { display: flex; flex-direction: column; line-height: 1; }
  .wordmark__name { font-size: 52px; letter-spacing: 3px; }
  .wordmark__tag { font-size: 14px; letter-spacing: 2.4px; margin-top: 6px; }
  .card--front .wordmark { color: var(--paper); }

  /* Back side */
  .card--back { background: var(--paper); }
  .card--back .wordmark {
    position: absolute; left: 62px; top: 120px;
    color: var(--ink); gap: 12px;
  }
  .card--back .wordmark__dot { width: 32px; height: 32px; background: var(--brand-blue); }
  .card--back .wordmark__name { font-size: 34px; letter-spacing: 2px; }
  .card--back .wordmark__tag { font-size: 9.5px; letter-spacing: 1.5px; margin-top: 4px; }

  .divider {
    position: absolute; left: 338px; top: 44px;
    width: 2px; height: 150px; background: var(--brand-blue);
  }
  .contact {
    position: absolute; left: 360px; top: 46px;
    color: var(--ink);
  }
  .contact__name { font-size: 20px; font-weight: 800; letter-spacing: 0.3px; }
  .contact__first { color: var(--brand-blue); }
  .contact__role { font-size: 14px; font-weight: 500; margin: 2px 0 14px; }
  .contact__list { list-style: none; font-size: 13.5px; font-weight: 500; }
  .contact__list li { display: flex; align-items: center; gap: 9px; margin-bottom: 7px; }
  .contact__icon { width: 15px; height: 15px; flex: none; fill: var(--brand-blue); }

  .wave { position: absolute; left: 0; bottom: 0; width: 100%; height: 170px; }
  .wave__fill { fill: var(--brand-blue); }
  .wave__line { fill: var(--ink); }
</style>
</head>
<body>
<main class="sheet">

  <section class="card card--front" aria-label="Card front">
    <div class="wordmark">
      <span class="wordmark__dot"></span>
      <span class="wordmark__text">
        <span class="wordmark__name">QUORVANE</span>
        <span class="wordmark__tag">SENSING SYSTEMS</span>
      </span>
    </div>
  </section>

  <section class="card card--back" aria-label="Card back">
    <div class="wordmark">
      <span class="wordmark__dot"></span>
      <span class="wordmark__text">
        <span class="wordmark__name">QUORVANE</span>
        <span class="wordmark__tag">SENSING SYSTEMS</span>
      </span>
    </div>

    <div class="divider"></div>

    <div class="contact">
      <p class="contact__name"><span class="contact__first">TOBIN</span> ASHGROVE</p>
      <p class="contact__role">Owner</p>
      <ul class="contact__list">
        <li>
          <svg class="contact__icon" viewBox="0 0 24 24" aria-hidden="true"><path d="M6.6 10.8a15 15 0 0 0 6.6 6.6l2.2-2.2a1 1 0 0 1 1-.25 11.4 11.4 0 0 0 3.6.57 1 1 0 0 1 1 1V20a1 1 0 0 1-1 1A17 17 0 0 1 3 4a1 1 0 0 1 1-1h3.5a1 1 0 0 1 1 1c0 1.25.2 2.45.57 3.57a1 1 0 0 1-.25 1z"/></svg>
          555.014.2290
        </li>
        <li>
          <svg class="contact__icon" viewBox="0 0 24 24" aria-hidden="true"><path d="M2 5h20v14H2zM3.5 6.5 12 13l8.5-6.5V8L12 14.5 3.5 8z"/></svg>
          info@quorvanesensing.com
        </li>
        <li>
          <svg class="contact__icon" viewBox="0 0 24 24" aria-hidden="true"><path d="M12 2a10 10 0 1 0 0 20 10 10 0 0 0 0-20zm6.9 6h-3a15 15 0 0 0-1.3-4 8 8 0 0 1 4.3 4zM12 4a13 13 0 0 1 1.9 4h-3.8A13 13 0 0 1 12 4zM4.3 14a8 8 0 0 1 0-4h3.4a16 16 0 0 0 0 4zm.8 2h3a15 15 0 0 0 1.3 4 8 8 0 0 1-4.3-4zm3-8h-3a8 8 0 0 1 4.3-4 15 15 0 0 0-1.3 4zM12 20a13 13 0 0 1-1.9-4h3.8A13 13 0 0 1 12 20zm2.3-6H9.7a14 14 0 0 1 0-4h4.6a14 14 0 0 1 0 4zm.3 5.9a15 15 0 0 0 1.3-3.9h3a8 8 0 0 1-4.3 3.9zm1.7-5.9a16 16 0 0 0 0-4h3.4a8 8 0 0 1 0 4z"/></svg>
          www.quorvanesensing.com
        </li>
      </ul>
    </div>

    <svg class="wave" viewBox="0 0 620 170" preserveAspectRatio="none" aria-hidden="true">
      <path class="wave__fill" d="M0 118 C 120 150, 230 150, 330 96 C 430 42, 520 10, 620 4 L620 170 L0 170 Z"/>
      <path class="wave__line" d="M150 146 C 250 146, 300 110, 360 78 C 440 36, 520 12, 600 2 C 520 16, 440 44, 366 84 C 300 120, 240 146, 150 146 Z"/>
    </svg>
  </section>

</main>
</body>
</html>
```